Flyer Design Project

Painting and Maintenance
This is what I have as idea as Job description
Refresh, renew & revive your home. from painting to carpentry. Do you guys have any epic unique slogan?
As what we do Residential - Commercial Interior - ExteriorTrim & Molding installationWainscoting - Wallpaper removalCabinet refinishing Woodwork EnamelingDeck & Fence Cleaning & SealingPressure washConcrete & Paver Washing
I would like to have a note that says-Prompt professional service-Free estimates-Insured -"visit us on PalPorch"
I would like new ideas from you guys as well!
Carpentry

```html
<!DOCTYPE html>
<html lang="en">
<head>
<meta charset="utf-8">
<title>Brightwell Painting &amp; Maintenance Flyer</title>
<link href="https://fonts.googleapis.com/css2?family=Ubuntu:wght@400;500;700&family=Roboto:wght@400;500;700&family=Libre+Baskerville:wght@700&display=swap" rel="stylesheet">
<style>
  :root {
    --red: #d12027;
    --dark: #3c3c3e;
    --ink: #2b2b2b;
    --paper: #ffffff;
    --mist: #ececec;
    --stage: #e6e3df;
    --social: #3b5a9a;
  }
  * { margin: 0; padding: 0; box-sizing: border-box; }
  html, body { width: 1200px; height: 1200px; overflow: hidden; background: var(--stage); }
  .canvas { position: relative; width: 1200px; height: 1200px; }

  .card { position: absolute; background: var(--paper); transform-origin: 0 0; transform: scale(0.8584); box-shadow: 0 6px 18px rgba(0,0,0,.25); overflow: hidden; }
  .card--front { left: 200px; top: 69px; width: 932px; height: 610px; }
  .card--back { left: 199px; top: 617px; width: 938px; height: 616px; }

  .shapes { position: absolute; inset: 0; }
  .abs { position: absolute; }

  .brand { font-family: "Ubuntu", sans-serif; font-weight: 700; color: var(--dark); text-align: center; line-height: 1; }
  .brand__name { display: block; }
  .brand__sub { display: block; }
  .brand--front { left: 551px; top: 50px; width: 240px; }
  .brand--front .brand__name { font-size: 40px; letter-spacing: 1px; }
  .brand--front .brand__sub { font-size: 15px; margin-top: 8px; letter-spacing: 1.5px; }

  .guide { left: 488px; top: 192px; font-family: "Ubuntu", sans-serif; font-weight: 500; font-size: 32px; color: var(--red); }
  .guide-rule { left: 662px; top: 216px; width: 222px; height: 2px; background: var(--red); }
  .headline-mid { left: 488px; top: 230px; font-family: "Libre Baskerville", serif; font-weight: 700; font-size: 31px; color: var(--ink); letter-spacing: .5px; }
  .headline-big { left: 486px; top: 266px; font-family: "Ubuntu", sans-serif; font-weight: 500; font-size: 50px; color: var(--red); letter-spacing: 1px; }

  .photo { border: 3px solid #111; }
  .photo--wall { left: 490px; top: 330px; width: 172px; height: 168px; background: linear-gradient(135deg, #f1ece2 0%, #e5ddcc 55%, #3e6fbd 100%); }
  .photo--deck { left: 713px; top: 330px; width: 173px; height: 168px; background: linear-gradient(180deg, #9aa39a 0%, #8a7a60 45%, #7a6448 100%); }
  .photo-divider { left: 687px; top: 330px; width: 2px; height: 168px; background: var(--red); }

  .phone-band { left: 448px; top: 515px; width: 484px; height: 62px; background: var(--red); display: flex; align-items: center; }
  .phone-band svg { margin-left: 50px; }
  .phone-band__number { margin-left: 30px; font-family: "Ubuntu", sans-serif; font-weight: 700; font-size: 48px; color: #fff; letter-spacing: 1px; }

  .back-bg { left: 0; top: 0; width: 938px; height: 420px; background: linear-gradient(180deg, #f4f4f4 0%, #e2e2e2 60%, #d8d8d8 100%); }

  .section-title { left: 0; width: 938px; top: 38px; text-align: center; font-family: "Roboto", sans-serif; font-weight: 500; font-size: 19px; color: var(--ink); }
  .section-title span { color: var(--red); }
  .section-title__rule { left: 407px; top: 63px; width: 126px; height: 2px; background: var(--dark); }

  .service { display: flex; align-items: center; gap: 20px; font-family: "Roboto", sans-serif; font-size: 15px; color: var(--ink); line-height: 1.2; }
  .service__icon { flex: none; width: 33px; height: 33px; border-radius: 50%; background: var(--red); display: flex; align-items: center; justify-content: center; }

  .shot { border: 3px solid var(--red); }
  .shot--paver { left: 154px; top: 251px; width: 175px; height: 128px; background: linear-gradient(160deg, #6d8a4f 0%, #8c8a84 40%, #55524c 100%); }
  .shot--pool { left: 360px; top: 236px; width: 218px; height: 158px; background: linear-gradient(180deg, #3f6b2c 0%, #6d9a4a 55%, #2f9bd8 78%, #c9c2b0 100%); }
  .shot--cabinet { left: 609px; top: 251px; width: 175px; height: 128px; background: linear-gradient(135deg, #6b3d22 0%, #4a2a18 50%, #d02a3a 100%); }

  .notes { left: 58px; top: 476px; font-family: "Roboto", sans-serif; font-size: 15px; color: var(--ink); line-height: 1.2; }
  .notes__line--ruled { display: inline-block; border-bottom: 1.5px solid var(--red); }
  .social { left: 59px; top: 526px; display: flex; align-items: center; gap: 12px; font-family: "Roboto", sans-serif; font-weight: 500; font-size: 18px; color: var(--red); }
  .social__mark { width: 27px; height: 27px; background: var(--social); }

  .call { left: 340px; top: 494px; width: 280px; text-align: center; font-family: "Roboto", sans-serif; }
  .call__label { display: inline-block; font-weight: 700; font-size: 21px; color: var(--red); border-bottom: 1.5px solid var(--dark); padding-bottom: 1px; }
  .call__number { margin-top: 8px; display: flex; align-items: center; justify-content: center; gap: 14px; font-weight: 500; font-size: 28px; color: var(--ink); letter-spacing: .5px; }

  .brand--back { left: 690px; top: 488px; width: 170px; }
  .brand--back .brand__name { font-size: 28px; }
  .brand--back .brand__sub { font-size: 10.5px; margin-top: 6px; letter-spacing: 1px; }
</style>
</head>
<body>
<div class="canvas">

  <section class="card card--front">
    <svg class="shapes" width="932" height="610" viewBox="0 0 932 610" aria-hidden="true">
      <polygon points="0,150 270,48 460,158 460,168 318,62 162,162 0,162" fill="#3c3c3e"/>
      <polyline points="0,168 166,168 318,70 460,168 932,168" fill="none" stroke="#d12027" stroke-width="9"/>
      <rect x="0" y="589" width="932" height="21" fill="#3c3c3e"/>
      <rect x="460" y="579" width="472" height="4" fill="#d12027"/>
    </svg>
    <div class="abs" role="img" aria-label="Photo of a large brick family home with trees and lawn"
         style="left:0;top:0;width:460px;height:589px;clip-path:polygon(0 176px,168px 176px,318px 80px,460px 176px,460px 589px,0 589px);background:linear-gradient(180deg,#3c7fd0 0%,#8fb4d8 30%,#a8958a 55%,#8a7a6c 75%,#5e8a3c 100%);"></div>

    <div class="abs brand brand--front">
      <span class="brand__name">BRIGHTWELL</span>
      <span class="brand__name">PAINTING</span>
      <span class="brand__sub">&amp; MAINTENANCE LLC.</span>
    </div>

    <div class="abs guide">A Guide To</div>
    <div class="abs guide-rule"></div>
    <div class="abs headline-mid">KEEPING YOUR HOME</div>
    <div class="abs headline-big">LOOKING GREAT</div>

    <div class="abs photo photo--wall" role="img" aria-label="Photo of a worker scraping an interior wall"></div>
    <div class="abs photo-divider"></div>
    <div class="abs photo photo--deck" role="img" aria-label="Photo of a worker pressure washing a wooden deck"></div>

    <div class="abs phone-band">
      <svg width="44" height="44" viewBox="0 0 24 24" aria-hidden="true"><path fill="#2b2b2b" d="M6.6 10.8c1.4 2.8 3.8 5.1 6.6 6.6l2.2-2.2c.3-.3.7-.4 1-.2 1.1.4 2.3.6 3.6.6.6 0 1 .4 1 1V20c0 .6-.4 1-1 1C10.6 21 3 13.4 3 4c0-.6.4-1 1-1h3.5c.6 0 1 .4 1 1 0 1.3.2 2.5.6 3.6.1.3 0 .7-.2 1z"/></svg>
      <span class="phone-band__number">555 014 2290</span>
    </div>
  </section>

  <section class="card card--back">
    <div class="abs back-bg" role="img" aria-label="Faint background photo of a house exterior"></div>

    <div class="abs section-title">WHAT <span>WE DO</span></div>
    <div class="abs section-title__rule"></div>

    <div class="abs service" style="left:61px;top:81px;">
      <span class="service__icon"><svg width="16" height="16" viewBox="0 0 16 16" aria-hidden="true"><rect x="2" y="2" width="12" height="12" fill="none" stroke="#fff" stroke-width="1.8"/><rect x="5" y="5" width="6" height="4" fill="#fff"/></svg></span>Commercial Interior</div>
    <div class="abs service" style="left:61px;top:124px;">
      <span class="service__icon"><svg width="16" height="16" viewBox="0 0 16 16" aria-hidden="true"><rect x="2" y="2" width="12" height="12" fill="#fff"/><path d="M2 6h12M2 10h12" stroke="#d12027" stroke-width="1.4"/></svg></span>Cabinet Refinishing</div>
    <div class="abs service" style="left:61px;top:169px;">
      <span class="service__icon"><svg width="16" height="16" viewBox="0 0 16 16" aria-hidden="true"><path d="M4 2v11M2 13h5" stroke="#fff" stroke-width="1.8"/><rect x="8" y="7" width="6" height="6" fill="#fff"/></svg></span>Sealing Pressure Wash</div>

    <div class="abs service" style="left:351px;top:80px;">
      <span class="service__icon"><svg width="16" height="16" viewBox="0 0 16 16" aria-hidden="true"><rect x="2" y="3" width="12" height="3" fill="#fff"/><rect x="5" y="8" width="6" height="6" fill="#fff"/></svg></span>Concrete &amp; Paver Washing</div>
    <div class="abs service" style="left:351px;top:124px;">
      <span class="service__icon"><svg width="16" height="16" viewBox="0 0 16 16" aria-hidden="true"><path d="M3 3l10 10M5 3h6" stroke="#fff" stroke-width="1.8"/></svg></span>Woodwork Enameling</div>
    <div class="abs service" style="left:351px;top:169px;">
      <span class="service__icon"><svg width="16" height="16" viewBox="0 0 16 16" aria-hidden="true"><rect x="2" y="3" width="12" height="10" fill="none" stroke="#fff" stroke-width="1.6"/><path d="M5 10l6-4" stroke="#fff" stroke-width="1.6"/></svg></span>Wallpaper Removal</div>

    <div class="abs service" style="left:649px;top:80px;">
      <span class="service__icon"><svg width="16" height="16" viewBox="0 0 16 16" aria-hidden="true"><path d="M2 5h12M2 11h12M4 3v11M8 3v11M12 3v11" stroke="#fff" stroke-width="1.6"/></svg></span>Deck &amp; Fence Cleaning</div>
    <div class="abs service" style="left:649px;top:124px;">
      <span class="service__icon"><svg width="16" height="16" viewBox="0 0 16 16" aria-hidden="true"><path d="M3 3l10 10M13 3L3 13" stroke="#fff" stroke-width="1.8"/></svg></span>ExteriorTrim &amp; Molding<br>Installation</div>

    <div class="abs shot shot--paver" role="img" aria-label="Photo of a paver patio being pressure washed"></div>
    <div class="abs shot shot--pool" role="img" aria-label="Photo of a backyard pool with a freshly cleaned fence"></div>
    <div class="abs shot shot--cabinet" role="img" aria-label="Photo of a worker refinishing bathroom cabinets"></div>

    <svg class="shapes" width="938" height="616" viewBox="0 0 938 616" aria-hidden="true">
      <polygon points="0,378 500,452 938,370 938,616 0,616" fill="#fff"/>
      <polyline points="0,376 500,450 938,368" fill="none" stroke="#3c3c3e" stroke-width="11"/>
      <polygon points="222,424 500,466 776,418 776,424 500,476 222,432" fill="#d12027"/>
      <rect x="0" y="592" width="938" height="4" fill="#d12027"/>
      <rect x="0" y="596" width="938" height="20" fill="#3c3c3e"/>
    </svg>

    <div class="abs notes">
      <div>Prompt professional service</div>
      <div class="notes__line--ruled">Free estimates-Insured</div>
    </div>
    <div class="abs social">Visit us on PalPorch <span class="social__mark"></span></div>

    <div class="abs call">
      <div class="call__label">CALL NOW</div>
      <div class="call__number">
        <svg width="24" height="24" viewBox="0 0 24 24" aria-hidden="true"><path fill="#d12027" d="M6.6 10.8c1.4 2.8 3.8 5.1 6.6 6.6l2.2-2.2c.3-.3.7-.4 1-.2 1.1.4 2.3.6 3.6.6.6 0 1 .4 1 1V20c0 .6-.4 1-1 1C10.6 21 3 13.4 3 4c0-.6.4-1 1-1h3.5c.6 0 1 .4 1 1 0 1.3.2 2.5.6 3.6.1.3 0 .7-.2 1z"/></svg>
        <span>555 014 2290</span>
      </div>
    </div>

    <div class="abs brand brand--back">
      <span class="brand__name">BRIGHTWELL</span>
      <span class="brand__name">PAINTING</span>
      <span class="brand__sub">&amp; MAINTENANCE LLC.</span>
    </div>
  </section>

</div>
</body>
</html>
```